Business card design needed

i am a small sized carpentry business looking to generate work in decks, pergolas, small renovations including bathroom renovations or overseeing new homes being built.

Carpentry

R K Carpentry
Marcus Ellery
0417382906
Specialize in quality decks, pergolas, small renovations including bathrooms and housing project management.
FREE QUOTES

```html
<!DOCTYPE html>
<html lang="en">
<head>
<meta charset="utf-8">
<title>R K Carpentry – Business Cards</title>
<link rel="stylesheet" href="https://fonts.googleapis.com/css2?family=Cinzel:wght@400&display=swap">
<style>
  :root {
    --backdrop: #e9e4dc;
    --card: #ffffff;
    --brand: #7b705f;
    --band: #776c5c;
    --band-light: #d9d7d4;
    --rule: #a59c8e;
  }
  * { margin: 0; padding: 0; box-sizing: border-box; }
  html, body {
    width: 1200px; height: 1113px; overflow: hidden;
    background: var(--backdrop);
    font-family: "Cinzel", "Times New Roman", serif;
    color: var(--brand);
  }
  .card {
    position: absolute;
    background: var(--card);
    overflow: hidden;
  }
  .card .wave { position: absolute; left: 0; top: 0; width: 100%; height: 100%; }

  /* front */
  .card--front { left: 56px; top: 74px; width: 712px; height: 438px; }
  .brand-mark {
    position: absolute;
    background: var(--brand);
  }
  .card--front .brand-mark { left: 32px; top: 34px; width: 86px; height: 84px; }
  .card--front .brand-name {
    position: absolute; left: 138px; top: 48px;
    font-size: 40px; letter-spacing: 1px; white-space: nowrap;
  }
  .tagline {
    position: absolute; left: 163px; top: 106px; width: 520px;
    font-size: 13px; line-height: 17px; text-align: center;
    text-transform: uppercase; letter-spacing: 0.2px;
  }
  .contact-name {
    position: absolute; right: 390px; top: 222px; text-align: right;
    font-size: 25px; line-height: 30px; white-space: nowrap;
  }
  .contact-role { display: block; font-size: 11px; line-height: 14px; }
  .divider {
    position: absolute; left: 411px; top: 202px;
    width: 2px; height: 74px; background: var(--rule);
  }
  .phone {
    position: absolute; left: 452px; top: 230px;
    display: flex; align-items: center; gap: 16px;
    font-size: 23px; white-space: nowrap;
  }
  .phone svg { width: 14px; height: 26px; }

  /* back */
  .card--back { left: 56px; top: 571px; width: 712px; height: 440px; }
  .card--back .brand-mark { left: 309px; top: 127px; width: 110px; height: 106px; }
  .card--back .brand-name {
    position: absolute; left: 0; right: 0; top: 243px; text-align: center;
    font-size: 44px; letter-spacing: 1px;
  }

  /* small */
  .card--mini { left: 831px; top: 829px; width: 312px; height: 182px; }
  .card--mini .brand-mark { left: 105px; top: 20px; width: 94px; height: 92px; }
  .card--mini .brand-name {
    position: absolute; left: 0; right: 0; top: 118px; text-align: center;
    font-size: 33px;
  }
</style>
</head>
<body>

<section class="card card--front">
  <svg class="wave" viewBox="0 0 712 438" preserveAspectRatio="none" aria-hidden="true">
    <path d="M0 250 C150 360 400 400 712 388 L712 438 L0 438 Z" fill="var(--band-light)"/>
    <path d="M0 268 C150 372 400 414 712 404 L712 438 L0 438 Z" fill="var(--band)"/>
  </svg>
  <div class="brand-mark" aria-hidden="true"></div>
  <div class="brand-name">R K Carpentry</div>
  <p class="tagline">Specialize in quality decks, pergolas, small renovations including bathrooms and housing project management</p>
  <div class="contact-name">Marcus Ellery<span class="contact-role">Manager</span></div>
  <div class="divider"></div>
  <div class="phone">
    <svg viewBox="0 0 14 26" aria-hidden="true">
      <rect x="1" y="1" width="12" height="24" rx="2" fill="none" stroke="var(--brand)" stroke-width="2"/>
      <rect x="3.5" y="4" width="7" height="7" fill="var(--brand)"/>
      <rect x="3.5" y="14" width="7" height="8" fill="var(--brand)" opacity="0.6"/>
    </svg>
    <span>0417382906</span>
  </div>
</section>

<section class="card card--back">
  <svg class="wave" viewBox="0 0 712 440" preserveAspectRatio="none" aria-hidden="true">
    <path d="M0 244 C150 354 400 396 712 382 L712 440 L0 440 Z" fill="var(--band-light)"/>
    <path d="M0 262 C150 368 400 410 712 400 L712 440 L0 440 Z" fill="var(--band)"/>
  </svg>
  <div class="brand-mark" aria-hidden="true"></div>
  <div class="brand-name">R K Carpentry</div>
</section>

<section class="card card--mini">
  <div class="brand-mark" aria-hidden="true"></div>
  <div class="brand-name">R K Carpentry</div>
</section>

</body>
</html>
```